Creative Businesss Card desgin!

Create a business card for our business Gleam window cleaning!
We are open to creative ideas as long as it maintains a professional image.

Target Market(s)

Small Commercial window cleaning clients including car dealerships, strata manager, cafe

Industry/Entity Type

Window Cleaning

Contact Information for Business Card

Daniel Prescott
General Manager
Gleam Window Cleaning

daniel@gleamservices.com.au
pane-care-southbank.com.au
Ph: 1800 GET GLEAM
Mob: 0437 582 061

Colors
fbed22
0392cd

Requirements
Should not have
• Stock window cleaning/ squeegee graphics

```html
<!DOCTYPE html>
<html lang="en">
<head>
<meta charset="utf-8">
<title>Gleam Window Cleaning – Business Card</title>
<link rel="stylesheet" href="https://fonts.googleapis.com/css2?family=Archivo:wght@400;700;800&display=swap">
<style>
  :root {
    --gleam-blue: #0392cd;
    --gleam-blue-deep: #0b5f93;
    --gleam-navy: #0d5a83;
    --gleam-yellow: #fbed22;
    --card-white: #f4f4f4;
    --stage: #2a2d31;
    --text-light: #ffffff;
  }
  * { box-sizing: border-box; margin: 0; padding: 0; }
  html, body {
    width: 1200px;
    height: 900px;
    overflow: hidden;
    background: var(--stage);
    font-family: "Archivo", "Helvetica Neue", Arial, sans-serif;
  }
  .canvas {
    width: 1200px;
    height: 900px;
    display: flex;
    align-items: center;
    justify-content: center;
  }
  .card {
    position: relative;
    width: 1000px;
    height: 611px;
    background: var(--card-white);
    overflow: hidden;
    box-shadow: 0 20px 50px rgba(0,0,0,0.45);
  }
  .card-art {
    position: absolute;
    inset: 0;
    width: 100%;
    height: 100%;
  }
  .brand-name {
    position: absolute;
    left: 70px;
    top: 62px;
    width: 460px;
    color: var(--gleam-navy);
    font-weight: 800;
    font-size: 56px;
    line-height: 1.02;
    letter-spacing: 1px;
    text-transform: uppercase;
  }
  .contact-block {
    position: absolute;
    right: 62px;
    bottom: 60px;
    text-align: right;
    color: var(--text-light);
  }
  .person-name {
    color: var(--gleam-yellow);
    font-weight: 700;
    font-size: 34px;
    letter-spacing: 1px;
    text-transform: uppercase;
    line-height: 1.1;
  }
  .person-role {
    font-size: 23px;
    font-weight: 400;
    margin-bottom: 26px;
  }
  .contact-list { list-style: none; }
  .contact-item {
    display: flex;
    justify-content: flex-end;
    align-items: center;
    gap: 12px;
    font-size: 23px;
    line-height: 1.4;
  }
  .contact-icon {
    width: 22px;
    height: 22px;
    flex: none;
    stroke: var(--gleam-yellow);
    fill: none;
    stroke-width: 2;
  }
</style>
</head>
<body>
<main class="canvas">
  <article class="card">
    <svg class="card-art" viewBox="0 0 1000 611" preserveAspectRatio="none" aria-hidden="true">
      <defs>
        <linearGradient id="blueField" x1="0" y1="0" x2="1" y2="1">
          <stop offset="0" stop-color="var(--gleam-blue)"/>
          <stop offset="1" stop-color="var(--gleam-blue-deep)"/>
        </linearGradient>
      </defs>
      <polygon class="accent-stripe" points="250,611 770,0 812,0 292,611" fill="var(--gleam-yellow)"/>
      <polygon class="blue-field" points="312,611 832,0 1000,0 1000,611" fill="url(#blueField)"/>
    </svg>

    <h1 class="brand-name">Gleam Window Cleaning</h1>

    <section class="contact-block">
      <p class="person-name">Daniel Prescott</p>
      <p class="person-role">General Manager</p>
      <ul class="contact-list">
        <li class="contact-item">1800 GET GLEAM
          <svg class="contact-icon" viewBox="0 0 24 24"><path d="M5 3l4 1 1 5-2 1a12 12 0 0 0 6 6l1-2 5 1 1 4-3 2C10 21 3 14 3 6z"/></svg>
        </li>
        <li class="contact-item">0437 582 061
          <svg class="contact-icon" viewBox="0 0 24 24"><rect x="6" y="2" width="12" height="20" rx="2"/><line x1="10" y1="18" x2="14" y2="18"/></svg>
        </li>
        <li class="contact-item">daniel@gleamservices.com.au
          <svg class="contact-icon" viewBox="0 0 24 24"><rect x="2" y="5" width="20" height="14"/><path d="M2 5l10 8 10-8"/></svg>
        </li>
        <li class="contact-item">pane-care-southbank.com.au
          <svg class="contact-icon" viewBox="0 0 24 24"><circle cx="12" cy="12" r="10"/><ellipse cx="12" cy="12" rx="4" ry="10"/><line x1="2" y1="12" x2="22" y2="12"/></svg>
        </li>
      </ul>
    </section>
  </article>
</main>
</body>
</html>
```